Dental Business Card

I need Dental oriented business cards.
On the front side -
- on the first line, my name:
Dr Marlo Vintner
- on the second line (just underneath):
Doctor of Dental Medicine
- on the third line, or underneath that or in a corner, I would like the address and phone number:
5182 Ch. Birchfield
Montreal QC H2T 4B9
514-629-5074
- other than that i would maybe like a logo of a tooth, but i want it to be subtle and very basic!
- I would like the card to be preferably black or dark grey-ish with the writing in white
On the other side -
- 2-3 lines with the possibility to write the next appointment the box with the lines should be white, with the rest of the card being black

```html
<!DOCTYPE html>
<html lang="en">
<head>
<meta charset="utf-8">
<title>Dental Business Card – Front and Back</title>
<link href="https://fonts.googleapis.com/css2?family=Work+Sans:wght@400;500;600&display=swap" rel="stylesheet">
<style>
  :root {
    --page-bg: #d9d7d4;
    --card-dark-top: #5a5a5a;
    --card-dark-bottom: #1e1e1e;
    --card-light: #ecebe8;
    --ink-light: #ffffff;
    --ink-dark: #3a3a3a;
    --rule-dark: #4a4a4a;
  }
  * { box-sizing: border-box; margin: 0; padding: 0; }
  html, body {
    width: 1200px; height: 901px; overflow: hidden;
    background: var(--page-bg);
    font-family: "Work Sans", Arial, sans-serif;
  }
  .sheet {
    width: 1200px; height: 901px;
    display: flex; align-items: center; justify-content: center; gap: 40px;
  }
  .card {
    width: 540px; height: 309px; position: relative;
    box-shadow: 0 6px 18px rgba(0,0,0,0.25);
  }

  /* Front */
  .card-front {
    background: linear-gradient(200deg, var(--card-dark-top) 0%, #3a3a3a 45%, var(--card-dark-bottom) 100%);
    color: var(--ink-light);
  }
  .front-block { position: absolute; left: 150px; top: 96px; width: 320px; }
  .front-name { font-size: 25px; font-weight: 600; letter-spacing: 0.5px; line-height: 1; }
  .front-title { font-size: 15px; font-weight: 400; letter-spacing: 0.6px; margin-top: 4px; margin-left: 14px; }
  .front-rule { width: 248px; height: 1px; background: var(--ink-light); margin: 14px 0 12px 14px; }
  .front-contact { font-size: 12.5px; letter-spacing: 0.8px; line-height: 1.75; }
  .front-phone { margin-left: 98px; }

  /* Back */
  .card-back { background: var(--card-light); color: var(--ink-dark); }
  .back-name { position: absolute; left: 44px; top: 34px; font-size: 28px; font-weight: 600; letter-spacing: 0.4px; line-height: 1; }
  .back-title { position: absolute; left: 58px; top: 66px; font-size: 19px; font-weight: 400; letter-spacing: 0.5px; }
  .appointment { position: absolute; left: 44px; right: 40px; top: 120px; font-size: 14px; letter-spacing: 0.6px; }
  .appointment-heading { margin-left: 150px; }
  .appointment-rule { height: 1px; background: var(--rule-dark); margin: 10px 0 0 150px; }
  .field-row { display: flex; align-items: flex-end; margin-top: 22px; }
  .field-label { white-space: nowrap; padding-right: 2px; }
  .field-line { flex: 1; height: 1px; background: var(--rule-dark); margin-bottom: 3px; }
  .field-gap { width: 2px; }
  .field-row.time { margin-top: 26px; }
  .field-row.time .field-line { flex: 0 0 240px; }
</style>
</head>
<body>
<main class="sheet">
  <section class="card card-front" aria-label="Business card front">
    <div class="front-block">
      <h1 class="front-name">DR MARLO VINTNER</h1>
      <p class="front-title">Doctor of Dental Medicine</p>
      <div class="front-rule"></div>
      <p class="front-contact front-phone">P : 514-629-5074</p>
      <p class="front-contact">A : 5182 Ch. Birchfield Montreal QC H2T 4B9</p>
    </div>
  </section>

  <section class="card card-back" aria-label="Business card back">
    <h2 class="back-name">DR MARLO VINTNER</h2>
    <p class="back-title">Doctor of Dental Medicine</p>
    <div class="appointment">
      <p class="appointment-heading">Next Appointment</p>
      <div class="appointment-rule"></div>
      <div class="field-row">
        <span class="field-label">Name,</span><span class="field-line"></span>
        <span class="field-gap"></span>
        <span class="field-label">Date,</span><span class="field-line"></span>
      </div>
      <div class="field-row time">
        <span class="field-label">Time,</span><span class="field-line"></span>
      </div>
    </div>
  </section>
</main>
</body>
</html>
```